Looking for something sharp classy and with an edge for an advanced civil construction business
Something that says professional
nothing too DARK

Target Market(s)

mining companies council civil contractors concrete works

Industry/Entity Type

Construction

Contact Information for Business Card

Brindle Civil Constructions
brindlecivilconstruction@quokkamail.com
Tavi Marlowe
0418275936

Font styles to use
Serif
Sans Serif

Colors
0455a3
0592cd
85cae6
000000
919191

Requirements
Must have
• On the back of the card must have
down the bottom small print email logo phone number

Should not have
• follow us on facebook
Brindle Civil Constructions

follow us on instagram
BRINDLECIVILCONSTRUCTIONS

```html
<!DOCTYPE html>
<html lang="en">
<head>
<meta charset="utf-8">
<title>Brindle Civil Constructions – Business Card</title>
<link href="https://fonts.googleapis.com/css2?family=Open+Sans:wght@400;600&family=Roboto+Condensed:wght@400;700&display=swap" rel="stylesheet">
<style>
  :root{
    --stage:#e8eaed;
    --card:#fbfcfd;
    --blue-deep:#0455a3;
    --blue:#0592cd;
    --blue-light:#85cae6;
    --black:#000000;
    --charcoal:#1d1f22;
    --grey:#919191;
    --text-grey:#5e6165;
    --white:#ffffff;
  }
  *{box-sizing:border-box;margin:0;padding:0}
  html,body{width:1200px;height:682px;overflow:hidden;background:var(--stage)}
  .canvas{position:relative;width:1200px;height:682px}

  .card{
    position:absolute;top:181px;width:560px;height:320px;overflow:hidden;
    box-shadow:0 8px 24px rgba(0,0,0,.18);
    font-family:"Open Sans",Arial,sans-serif;
  }
  .card--front{left:27px;background:var(--card);color:var(--black)}
  .card--back{left:613px;background:var(--charcoal);color:var(--white)}

  /* front */
  .top-rule{position:absolute;left:0;top:0;width:440px;height:8px;background:linear-gradient(90deg,var(--blue-deep),var(--blue))}
  .corner-block{position:absolute;right:0;top:0;width:24px;height:22px;background:var(--charcoal)}
  .title-band{
    position:absolute;right:0;top:22px;width:190px;height:26px;
    background:linear-gradient(90deg,var(--blue),var(--blue-deep));
    color:var(--white);font-family:"Roboto Condensed",Arial,sans-serif;
    font-size:13px;letter-spacing:1.5px;line-height:26px;padding-left:20px;
  }
  .brand{position:absolute;left:40px;top:82px;display:flex;align-items:center;gap:12px}
  .brand-square{width:34px;height:34px;background:var(--blue-deep)}
  .brand-name{font-weight:600;font-size:20px;color:var(--blue-deep);line-height:1.1}
  .name-band{
    position:absolute;left:0;top:148px;width:320px;height:38px;
    background:linear-gradient(90deg,var(--blue-deep),var(--blue));
    display:flex;align-items:center;
  }
  .name-icon{width:38px;height:38px;background:var(--charcoal);display:flex;align-items:center;justify-content:center}
  .person-name{
    font-family:"Roboto Condensed",Arial,sans-serif;font-weight:700;
    color:var(--white);font-size:21px;letter-spacing:1.5px;padding-left:16px;
  }
  .contacts{
    position:absolute;left:64px;top:208px;display:grid;
    grid-template-columns:140px auto;row-gap:12px;column-gap:18px;
    font-size:11px;color:var(--text-grey);
  }
  .contact{display:flex;align-items:center;gap:8px;white-space:nowrap}
  .contact svg{flex:none}
  .left-accent{position:absolute;left:0;bottom:36px;width:14px;height:72px;background:var(--blue-deep)}
  .address-band{
    position:absolute;left:0;bottom:0;width:100%;height:36px;background:var(--charcoal);
    color:var(--white);font-size:11px;display:flex;align-items:center;gap:9px;padding-left:40px;
  }

  /* back */
  .back-rule{position:absolute;left:0;top:0;width:100%;height:8px;background:linear-gradient(90deg,var(--blue-deep),var(--blue))}
  .back-accent{position:absolute;right:0;top:8px;width:120px;height:4px;background:var(--blue-light)}
  .back-brand{
    position:absolute;left:0;right:0;top:118px;display:flex;align-items:center;justify-content:center;gap:12px;
  }
  .back-brand .brand-square{background:var(--blue)}
  .back-brand .brand-name{color:var(--white)}
  .back-line{position:absolute;left:200px;top:176px;width:160px;height:2px;background:var(--blue)}
  .small-print{
    position:absolute;left:0;right:0;bottom:18px;text-align:center;
    font-size:9.5px;color:var(--grey);letter-spacing:.3px;
  }
  .small-print .sep{color:var(--blue-light);padding:0 8px}
</style>
</head>
<body>
<div class="canvas">
  <article class="card card--front">
    <div class="top-rule"></div>
    <div class="corner-block"></div>
    <div class="title-band">GENERAL MANAGER</div>

    <div class="brand">
      <div class="brand-square"></div>
      <div class="brand-name">Brindle Civil Constructions</div>
    </div>

    <div class="name-band">
      <div class="name-icon">
        <svg width="18" height="18" viewBox="0 0 30 30" aria-hidden="true">
          <circle cx="15" cy="10" r="6" fill="#fff"/>
          <path d="M4 27c0-7 5-10 11-10s11 3 11 10z" fill="#fff"/>
        </svg>
      </div>
      <div class="person-name">TAVI MARLOWE</div>
    </div>

    <div class="contacts">
      <div class="contact">
        <svg width="11" height="11" viewBox="0 0 24 24" aria-hidden="true"><path d="M6 2h4l2 5-3 2a12 12 0 0 0 6 6l2-3 5 2v4a2 2 0 0 1-2 2A18 18 0 0 1 4 4a2 2 0 0 1 2-2z" fill="#0455a3"/></svg>
        <span>0418 275 936</span>
      </div>
      <div class="contact">
        <svg width="11" height="11" viewBox="0 0 24 24" aria-hidden="true"><rect x="2" y="5" width="20" height="14" fill="#0455a3"/><path d="M2 5l10 8 10-8" stroke="#fff" stroke-width="2" fill="none"/></svg>
        <span>brindlecivilconstruction@quokkamail.com</span>
      </div>
      <div class="contact">
        <svg width="11" height="11" viewBox="0 0 24 24" aria-hidden="true"><rect x="6" y="2" width="12" height="20" rx="2" fill="#0455a3"/><rect x="8" y="5" width="8" height="12" fill="#fff"/></svg>
        <span>0418 275 936</span>
      </div>
      <div class="contact">
        <svg width="11" height="11" viewBox="0 0 24 24" aria-hidden="true"><circle cx="12" cy="12" r="10" fill="none" stroke="#0455a3" stroke-width="2"/><path d="M2 12h20M12 2c4 4 4 16 0 20M12 2c-4 4-4 16 0 20" stroke="#0455a3" stroke-width="1.6" fill="none"/></svg>
        <span>www.brindlecivilworks.net</span>
      </div>
    </div>

    <div class="left-accent"></div>
    <div class="address-band">
      <svg width="11" height="15" viewBox="0 0 18 24" aria-hidden="true"><path d="M9 0a9 9 0 0 0-9 9c0 7 9 15 9 15s9-8 9-15a9 9 0 0 0-9-9z" fill="#fff"/><circle cx="9" cy="9" r="3.5" fill="#1d1f22"/></svg>
      <span>42 Quarry Road, Level 3, Ironbark St</span>
    </div>
  </article>

  <article class="card card--back">
    <div class="back-rule"></div>
    <div class="back-accent"></div>
    <div class="back-brand">
      <div class="brand-square"></div>
      <div class="brand-name">Brindle Civil Constructions</div>
    </div>
    <div class="back-line"></div>
    <p class="small-print">brindlecivilconstruction@quokkamail.com<span class="sep">|</span>Brindle Civil Constructions<span class="sep">|</span>0418 275 936</p>
  </article>
</div>
</body>
</html>
```